A5, portrait
Theme is science
audience is VIPS, politicians, executives
this is a really important event, we want a very classy invitation
include logo for brook and bloom and nexa but nexa one bigger
images attached
Have attached some styles we like but doesn't need to be these colours. If we can incorporate some colours from our logo would be good but don't make too colourful and childish

You’re invited to the official opening and launch of Nexa, Centre of Wonderment. an industry first, pioneering, STEM hub.

Saturday 30th April, 2022

10:00 am – 12:00 pm

42 Pellow Street, Hadley Vale

Light canapes provided. Dress code is smart/casual

All guests will be given a guided walk through of Australia’s first dedicated STEM education hub for children aged 3-6.

Invitation only

RSVP: 18 April to marketing@brookandbloom.edu.au

```html
<!DOCTYPE html>
<html lang="en">
<head>
<meta charset="utf-8">
<title>Nexa Launch Invitation</title>
<link rel="stylesheet" href="https://fonts.googleapis.com/css2?family=Mulish:wght@300;400;600;700;800&family=Gochi+Hand&display=swap">
<style>
  :root {
    --stage: #a9a9a9;
    --ink-top: #3b3036;
    --ink-mid: #201c21;
    --ink-low: #16141c;
    --violet: #2a2657;
    --violet-deep: #1d1a3a;
    --gold: #c99a5b;
    --gold-pale: #e0c08e;
    --rule: #bdb6b4;
    --text: #ffffff;
    --ribbon: #f07b2e;
    --ribbon-text: #2b2120;
    --rsvp: #f6d40c;
    --nexa: #ffffff;
  }
  * { margin: 0; padding: 0; box-sizing: border-box; }
  html, body { width: 1200px; height: 1200px; overflow: hidden; }
  body {
    background: var(--stage);
    font-family: "Mulish", sans-serif;
    color: var(--text);
    position: relative;
  }
  .invitation {
    position: absolute;
    left: 245px; top: 96px;
    width: 710px; height: 1007px;
    overflow: hidden;
    background: linear-gradient(180deg, var(--ink-top) 0%, var(--ink-mid) 45%, var(--ink-low) 70%, var(--ink-low) 100%);
  }
  .pattern-field {
    position: absolute; inset: 0;
    background: radial-gradient(ellipse at 50% 40%, rgba(0,0,0,0) 55%, rgba(201,154,91,0.12) 100%);
  }
  .panel {
    position: absolute;
    left: 87px; top: 83px; width: 536px; height: 842px;
    background: linear-gradient(180deg, #3a3036 0%, #211d22 50%, #16141b 100%);
  }
  .photo {
    position: absolute;
    left: 0; right: 0; top: 650px; bottom: 0;
    background:
      radial-gradient(circle at 52% 38%, #8a86ff 0%, #4a46c8 10%, rgba(40,36,110,0.7) 19%, rgba(22,20,40,0) 38%),
      linear-gradient(180deg, rgba(22,20,28,0) 0%, var(--violet) 40%, var(--violet-deep) 100%);
  }
  .frame { position: absolute; inset: 0; pointer-events: none; }
  .content { position: absolute; inset: 0; text-align: center; }
  .rule {
    position: absolute; left: 137px; width: 442px; height: 1px;
    background: linear-gradient(90deg, rgba(189,182,180,0.2), var(--rule), rgba(189,182,180,0.2));
  }
  .rule--top { top: 138px; }
  .rule--bottom { top: 261px; }
  .intro {
    position: absolute; top: 152px; left: 0; right: 0;
    font-size: 22px; line-height: 30px; font-weight: 600; letter-spacing: 0.2px;
  }
  .date {
    position: absolute; top: 294px; left: 0; right: 0;
    font-size: 36px; font-weight: 800; letter-spacing: 0.3px;
  }
  .time, .address {
    position: absolute; left: 0; right: 0;
    font-size: 32px; font-weight: 400; letter-spacing: 0.4px;
  }
  .time { top: 343px; }
  .address { top: 391px; }
  .ribbon {
    position: absolute; left: 119px; top: 445px; width: 482px; height: 50px;
  }
  .ribbon svg { position: absolute; inset: 0; }
  .ribbon span {
    position: relative; display: block; line-height: 50px;
    font-size: 16px; font-weight: 700; color: var(--ribbon-text);
  }
  .details {
    position: absolute; top: 518px; left: 0; right: 0;
    font-size: 16.5px; line-height: 21.5px; font-weight: 600;
  }
  .rsvp {
    position: absolute; top: 600px; left: 0; right: 0;
    font-size: 19px; color: var(--rsvp); font-weight: 400;
  }
  .rsvp strong { font-weight: 800; }
  .access {
    position: absolute; top: 645px; left: 0; right: 0;
    display: flex; justify-content: center; align-items: center; gap: 10px;
    font-family: "Gochi Hand", cursive; font-size: 46px; line-height: 1;
  }
  .brand {
    position: absolute; text-align: center; font-family: "Mulish", sans-serif;
    color: var(--nexa); font-weight: 800; white-space: nowrap;
  }
  .brand--nexa { left: 440px; top: 750px; width: 180px; font-size: 52px; line-height: 60px; letter-spacing: 2px; }
  .brand--bb { left: 440px; top: 870px; width: 180px; font-size: 17px; line-height: 22px; }
</style>
</head>
<body>
  <main class="invitation">
    <div class="pattern-field" role="img" aria-label="Faint gold line-icon pattern of science symbols: flasks, molecules, DNA strands and beakers"></div>
    <div class="panel"></div>
    <div class="photo" role="img" aria-label="Photograph of a glowing blue plasma ball on a black plinth in a dim room"></div>

    <svg class="frame" width="710" height="1007" viewBox="0 0 710 1007" aria-hidden="true">
      <defs>
        <linearGradient id="goldLine" x1="0" y1="0" x2="1" y2="1">
          <stop offset="0" stop-color="#e0c08e"/>
          <stop offset="0.5" stop-color="#b9874a"/>
          <stop offset="1" stop-color="#e0c08e"/>
        </linearGradient>
      </defs>
      <rect x="68" y="64" width="573" height="880" fill="none" stroke="url(#goldLine)" stroke-width="3"/>
      <rect x="74" y="70" width="561" height="868" fill="none" stroke="url(#goldLine)" stroke-width="1.2"/>
      <rect x="81" y="77" width="547" height="854" fill="none" stroke="url(#goldLine)" stroke-width="1.2"/>
      <rect x="88" y="84" width="533" height="840" fill="none" stroke="#c9c2c0" stroke-opacity="0.5" stroke-width="0.8"/>
    </svg>

    <div class="content">
      <div class="rule rule--top"></div>
      <p class="intro">You're invited to the official opening<br>and launch of Nexa, Centre of Wonderment.<br>an industry first, pioneering, STEM hub.</p>
      <div class="rule rule--bottom"></div>

      <p class="date">Saturday 30th April, 2022</p>
      <p class="time">10:00 am – 12:00 pm</p>
      <p class="address">42 Pellow Street, Hadley Vale</p>

      <div class="ribbon">
        <svg width="482" height="50" viewBox="0 0 482 50" aria-hidden="true">
          <polygon points="0,0 482,0 460,25 482,50 0,50 22,25" fill="var(--ribbon)"/>
        </svg>
        <span>Light canapes provided. Dress code is smart/casual</span>
      </div>

      <p class="details">All guests will be given a guided<br>walk through of Australia's first dedicated<br>STEM education hub for children aged 3-6.</p>

      <p class="rsvp"><strong>RSVP:</strong> 18 April to marketing@brookandbloom.edu.au</p>

      <div class="access">
        <svg width="34" height="36" viewBox="0 0 34 36" aria-hidden="true">
          <rect x="6" y="2" width="22" height="20" fill="#fff3c4"/>
          <polygon points="17,6 19,11 24,11 20,14 21.5,19 17,16 12.5,19 14,14 10,11 15,11" fill="#f6c90e" stroke="#2b2120" stroke-width="0.8"/>
          <polygon points="1,14 17,26 33,14 33,35 1,35" fill="#f6c90e"/>
          <polyline points="1,35 17,23 33,35" fill="none" stroke="#fff3c4" stroke-width="1.5"/>
        </svg>
        <span>Invitation only</span>
      </div>

      <p class="brand brand--nexa">Nexa</p>
      <p class="brand brand--bb">Brook and Bloom</p>
    </div>
  </main>
</body>
</html>
```